Become the head packaging designer of Tolvenu: Desing our vacuumbag packaging

Become the head designer of Tolvenu. A new brand of household products.

BRAND:
Tolvenu is our new brand which consists of accessories and spareparts of home appliances. These are products like vacuumbags, descalers, toothbrush heads, waterfilters for your frigde. So a lot of products that are consumed by household appliances. Tolvenu is positioned as being 'good quality, fair prices' (best buy). Important aspect is that the packaging should communicate that the products are of high quality. Most products are alternatives to original products so therefore the customer should be convinced they are buying products of the same or better quality as the original, but for better prices.

PRODUCT:
The first productline we are going to introduce is vacuumbags. These are alternative to the original bags of the manufacturer. The market position is 'good quality, low prices' (best buy). Details further below.

FUTURE DESIGNS:
We want to consider the winner as our packaging designer if we can agree on a fair price and if we're in line concerning the designs. That is why I want to consider the vacuumbags as a pilot.

DETAILS FOR THIS DESIGN:
- It will be several different bags (about 8) which are designed for different vacuumcleaners. Goal is to have one universal design with some variable elements we can adjust ourselves.
- The bags will be packaged by 4 pieces and will be in a plastic sealed bag. On this plastic bag will be a A5-sticker in colors with the design on it.
- The design should be a fresh, clear design and fitting for the target audience and market position.
- The elements which should be on there are:
(1) Our logo
(2) Pictures with text of aspects of the bags: super hygienic, high performance (good sucking power of vacuumcleaner), microfibre quality, 2x durability (can be used two times a standard paper vacuumbag can be used)
(3) Picture of microfibre vacuumbags
(4) Number of bags in packaging: 4
(5) Brandname(s) (for which the vacuumbag is suited. f.e. Korpa, KTR, Fenlo). - VARIABLE
(6) QR code - VARIABLE
(7) SKU (articlenumber) - VARIABLE
(8) Barcode - VARIABLE

Comparable product(s) (NOT for design):
http://www.tramvel.nl/nl/trmnl/huishoudelijk-en-schoonmaak/stofzuigerzakken/korvest/kv42-duraweefplus-stofzuigerzakken
http://www.durap.nl/winkel/huis-en-tuin/huis/huishoudelijk/stofzuigers/stofzuigerzakken-korvest-q-zak-(48213976)
http://www.zakkenwinkelier.com/ktr-vm-24-37.html

Target Market(s)

Typical households. B2C (end-consumers).

Requirements
Must have
• Quality, fresh, distinctive design.
Should not have
• Old-fashioned or cheap feeling.

```html
<!DOCTYPE html>
<html lang="en">
<head>
<meta charset="utf-8">
<title>Tolvenu Vacuum Bag Pack</title>
<link rel="stylesheet" href="https://fonts.googleapis.com/css2?family=Open+Sans:wght@400;600;700&display=swap">
<style>
  :root {
    --brand-red: #e8363a;
    --red-soft: #f07a7c;
    --white: #ffffff;
    --outline: #c9c9c9;
    --page: #ffffff;
  }
  html, body {
    margin: 0;
    padding: 0;
    width: 744px;
    height: 1200px;
    overflow: hidden;
    background: var(--page);
  }
  .canvas {
    position: relative;
    width: 744px;
    height: 1200px;
    font-family: "Open Sans", Arial, sans-serif;
  }
  .hanger {
    position: absolute;
    left: 0;
    top: 0;
  }
  .pack {
    position: absolute;
    left: 45px;
    top: 174px;
    width: 654px;
    height: 992px;
    box-sizing: border-box;
    border: 2px solid var(--outline);
    border-top: none;
    background: var(--white);
    overflow: hidden;
  }
  .brand-name {
    position: absolute;
    left: 64px;
    top: 80px;
    margin: 0;
    font-family: "Open Sans", Arial, sans-serif;
    font-weight: 700;
    font-size: 56px;
    line-height: 1;
    color: var(--brand-red);
  }
  .intro {
    position: absolute;
    left: 64px;
    top: 194px;
    margin: 0;
    color: var(--brand-red);
    font-size: 15px;
    line-height: 22px;
  }
  .intro .small {
    font-size: 12px;
    line-height: 18px;
    color: var(--red-soft);
    display: block;
  }
  .red-panel {
    position: absolute;
    left: 0;
    top: 401px;
    width: 100%;
    height: 591px;
    background: var(--brand-red);
  }
  .quality {
    position: absolute;
    left: 40px;
    top: 68px;
    display: flex;
    align-items: center;
    gap: 10px;
    color: var(--white);
  }
  .quality-label {
    font-size: 15px;
    line-height: 19px;
    font-weight: 600;
  }
  .quality-stars {
    display: block;
    font-size: 10px;
    letter-spacing: 3px;
    margin-top: 2px;
  }
  .quantity {
    position: absolute;
    left: 240px;
    top: 62px;
    width: 60px;
    height: 60px;
    border: 3px solid var(--white);
    border-radius: 50%;
    box-sizing: border-box;
    color: var(--white);
    font-size: 24px;
    font-weight: 600;
    display: flex;
    align-items: center;
    justify-content: center;
  }
  .bag-visual {
    position: absolute;
    left: 165px;
    top: 150px;
    width: 375px;
    height: 270px;
    background: linear-gradient(135deg, #ee5558, #e23034);
    border: 2px solid rgba(255,255,255,0.55);
    box-sizing: border-box;
  }
</style>
</head>
<body>
<div class="canvas">
  <svg class="hanger" width="744" height="176" viewBox="0 0 744 176" aria-hidden="true">
    <polygon points="45,176 45,110 150,45 594,45 699,110 699,176" fill="#ffffff" stroke="#c9c9c9" stroke-width="2"/>
    <rect x="330" y="84" width="84" height="22" rx="11" fill="#ffffff" stroke="#c9c9c9" stroke-width="2"/>
  </svg>

  <main class="pack">
    <h1 class="brand-name">Tolvenu</h1>

    <p class="intro">
      Lorem ipsum dolor sit amet<br>
      <span class="small">consectetur adipiscing elit, sed do eiusmo</span>
      ut labore et dolore magna aliqua<br>
      <span class="small">ut enim ad minim veniam</span>
      quis nostrud exercitation ullamco laboris<br>
      <span class="small">nisi ut aliquip ex ea commodo consequat</span>
    </p>

    <section class="red-panel">
      <div class="quality">
        <div class="quality-label">Microfibre<br>Quality<span class="quality-stars">★★★★</span></div>
        <svg width="50" height="50" viewBox="0 0 50 50" aria-hidden="true">
          <circle cx="25" cy="25" r="22" fill="none" stroke="#ffffff" stroke-width="3"/>
        </svg>
      </div>
      <div class="quantity">4X</div>
      <div class="bag-visual" role="img" aria-label="Line illustration of a microfibre vacuum bag with its card collar"></div>
    </section>
  </main>
</div>
</body>
</html>
```